Vornex-Dal Manufacturing Finishing Capabilities

A brochure selling metal finishing capabilities.
The finishing capabilities include
• Anodizing Black, Clear, Color, Type II and III - MIL-A-8625.
• Bright Dip Color Brilliant Anodizing
• Shot Peening Enhances surface finish and enhance fatigue strength of component
• Passivation ASTM A967/A967M-13 Nitric 3, ASTM A967/A967M-13 Nitric 4 - Improve corrosion resistance
• Electropolishing Shiny or Matte finish
• Clear Chemical Conversion Coating MIL-DTL-5541 Type II Class 1A & Class 3 - Improve adhesion for paint and primers.
Please refer to the attached banner file, brochure, anodize/bright dip color palette. Website www.vornexdalco.com specifically the tab http://vornexdalco.com/anodizing/ DO NOT INCLUDE THE PICTURE OF ANODIZE LINE IN THE BROCHURE
Locate part pictures online showing finished anodized, bright dipped brilliant colors, shot peening, passivation, electropolishing and Clear Chemical Conversion Coating.

```html
<!DOCTYPE html>
<html lang="en">
<head>
<meta charset="utf-8">
<title>Vornex-Dal Manufacturing – Finishing Capabilities</title>
<link rel="stylesheet" href="https://fonts.googleapis.com/css2?family=Lato:wght@400;700;900&display=swap">
<style>
  :root {
    --backdrop: #5b5b5b;
    --paper: #ffffff;
    --panel: #ececec;
    --brand-navy: #1d2a44;
    --brand-blue: #2f6aae;
    --heading-blue: #1f5b9e;
    --ink: #2b2b2b;
    --footer-bar: #58585a;
    --rule: #8a8a8a;
  }
  * { margin: 0; padding: 0; box-sizing: border-box; }
  html, body { width: 1200px; height: 1200px; overflow: hidden; background: var(--backdrop); }
  body { position: relative; font-family: "Lato", sans-serif; }

  .flyer {
    position: absolute; left: 172px; top: 0;
    width: 874px; height: 1226px;
    background: var(--paper);
    transform: scale(0.9788); transform-origin: 0 0;
    overflow: hidden;
  }
  .brand {
    position: absolute; top: 0; left: 0; width: 100%; height: 178px;
    display: flex; flex-direction: column; align-items: center; justify-content: center;
    color: var(--brand-navy); font-weight: 900; text-transform: uppercase; text-align: center;
  }
  .brand-name { font-size: 40px; letter-spacing: 2px; line-height: 1.1; }
  .brand-sub { font-size: 18px; letter-spacing: 12px; line-height: 1.4; margin-right: -12px; }

  .hero {
    position: absolute; top: 178px; left: 0; width: 100%; height: 534px;
    background: radial-gradient(ellipse at 65% 35%, #b9cde0 0%, #4a6c8e 22%, #1d3450 50%, #0c1420 85%);
  }
  .hero-band { position: absolute; top: 712px; left: 0; width: 100%; height: 28px; background: var(--brand-blue); }
  .content { position: absolute; top: 740px; left: 0; width: 100%; height: 386px; background: var(--panel); }

  .thumb {
    position: absolute; top: 613px; width: 224px; height: 186px;
    background: var(--paper); padding: 8px;
    box-shadow: 0 3px 6px rgba(0,0,0,.35);
  }
  .thumb-fill { width: 100%; height: 100%; }
  .thumb-parts { left: 66px; }
  .thumb-parts .thumb-fill { background: linear-gradient(135deg, #e6e6e6, #3a3a3a 45%, #1a1a1a 60%, #d8d8d8); }
  .thumb-spray { left: 317px; }
  .thumb-spray .thumb-fill { background: linear-gradient(120deg, #4b4b4b, #a8a8a8 45%, #5e5e5e); }
  .thumb-mill { left: 567px; }
  .thumb-mill .thumb-fill { background: linear-gradient(180deg, #cfc7bd, #8c8a86 55%, #a9b9b4); }

  .caps-title {
    position: absolute; top: 833px; left: 21px;
    font-size: 22px; font-weight: 700; color: var(--heading-blue);
  }
  .caps-list { position: absolute; list-style: none; color: var(--ink); font-size: 18px; line-height: 23px; }
  .caps-list li { position: absolute; left: 0; display: flex; gap: 7px; width: 100%; }
  .caps-list svg { flex: none; width: 19px; height: 19px; margin-top: 2px; }
  .caps-left { left: 21px; top: 886px; width: 420px; }
  .caps-right { left: 475px; top: 888px; width: 390px; }
  .caps-divider { position: absolute; left: 451px; top: 886px; width: 1px; height: 237px; background: var(--rule); }

  .footer-bar {
    position: absolute; top: 1151px; left: 0; width: 100%; height: 48px;
    background: var(--footer-bar);
    display: flex; align-items: center; justify-content: center;
    color: #fff; font-size: 30px; font-weight: 700; letter-spacing: 5px;
  }
</style>
</head>
<body>
<svg width="0" height="0" style="position:absolute">
  <symbol id="tick" viewBox="0 0 20 20">
    <circle cx="10" cy="10" r="8.6" fill="none" stroke="#2b2b2b" stroke-width="1.5"/>
    <path d="M5.8 10.3l2.8 2.8 5.6-6" fill="none" stroke="#2b2b2b" stroke-width="1.6" stroke-linecap="round" stroke-linejoin="round"/>
  </symbol>
</svg>

<main class="flyer">
  <header class="brand">
    <div class="brand-name">Vornex-Dal</div>
    <div class="brand-sub">Manufacturing</div>
  </header>

  <div class="hero" role="img" aria-label="Close-up photo of a lathe machining a metal shaft with coolant and flying chips"></div>
  <div class="hero-band"></div>
  <section class="content"></section>

  <figure class="thumb thumb-parts"><div class="thumb-fill" role="img" aria-label="Photo of black anodized aluminium heat sink parts"></div></figure>
  <figure class="thumb thumb-spray"><div class="thumb-fill" role="img" aria-label="Photo of a spray gun coating hanging metal parts"></div></figure>
  <figure class="thumb thumb-mill"><div class="thumb-fill" role="img" aria-label="Photo of a CNC milling machine cutting a part with coolant"></div></figure>

  <h2 class="caps-title">Finishing Capabilities Include:</h2>

  <ul class="caps-list caps-left">
    <li style="top:0"><svg><use href="#tick"/></svg><span>Anodizing Black, Clear, Color, Type II and III - MIL-A-8625.</span></li>
    <li style="top:68px"><svg><use href="#tick"/></svg><span>Bright Dip Color Brilliant Anodizing</span></li>
    <li style="top:109px"><svg><use href="#tick"/></svg><span>Shot Peening Enhances surface finish and enhance fatigue strength of component</span></li>
    <li style="top:176px"><svg><use href="#tick"/></svg><span>Passivation ASTM A967/A967M-13 Nitric 3, ASTM A967/A967M-13 Nitric 4</span></li>
  </ul>

  <div class="caps-divider"></div>

  <ul class="caps-list caps-right">
    <li style="top:0"><svg><use href="#tick"/></svg><span>Improve corrosion resistance</span></li>
    <li style="top:39px"><svg><use href="#tick"/></svg><span>Electropolishing Shiny or Matte finish</span></li>
    <li style="top:80px"><svg><use href="#tick"/></svg><span>Clear Chemical Conversion Coating MIL-DTL-5541 Type II Class 1A &amp; Class 3 -</span></li>
    <li style="top:145px"><svg><use href="#tick"/></svg><span>Improve adhesion for paint and primers.</span></li>
  </ul>

  <footer class="footer-bar">www.vornexdalco.com</footer>
</main>
</body>
</html>
```